April 11th Event- Islamorada- Coaching/Tarot/Hypnotherapy

Hi! Need a flyer that can also be posted on social media. Directions attached. Also will need a version that 2 can fit on 1 piece of paper so I can cut in half for hand outs. PDF example attached as well so you can understand. Thank you!

AAAAAAAAAAAAAAAAAAAAAAAAAAAAAAAAAAAAAAAAAAAAAAAAAAAAAAAAAAAAAAAAAAAAAAAAAAAAAAAAAAAAAAAAAAAAAAAAAAAAAAAAAAAAAAAAAAAAAAAAAAAAAAAAAAAAAAAAAAAAAAAAAAAAAAAAAAAAAAAAAAAAAAAAAAAAAAAAAAAAAAAAAAAAAAAAAAAAAAAAAAAAAAAAAAAAAAAAAAAAAAAAAA

Target Market(s)

Female audience age 35-70.
Spiritual, sophisticated

Industry/Entity Type

Event Planning

Font styles to use
Serif

Colors
d2a4cc
3176b5
85acd3
b868aa
e667a6
eea4c8
f59296
fbf289
add136

Requirements
Must have
• See attachments
Nice to have
• See attachments

```html
<!DOCTYPE html>
<html lang="en">
<head>
<meta charset="utf-8">
<title>Get The 411 – Evening of Self Discovery</title>
<link href="https://fonts.googleapis.com/css2?family=Playball&family=Josefin+Sans:wght@400;600;700&display=swap" rel="stylesheet">
<style>
  :root{
    --plum:#b05ca6;
    --orchid:#b868aa;
    --band:#c27db4;
    --rose:#e667a6;
    --blush:#eea4c8;
    --box-bg:#fbeaf4;
    --blue:#3176b5;
    --yellow:#fbf289;
    --ink:#111;
    --white:#fff;
  }
  *{box-sizing:border-box;margin:0;padding:0}
  html,body{width:960px;height:1200px;overflow:hidden;background:var(--white)}
  body{font-family:"Josefin Sans",sans-serif;color:var(--ink);position:relative}
  .flyer{position:relative;width:960px;height:1200px;overflow:hidden}
  .title{position:absolute;top:18px;width:100%;text-align:center;font-family:"Playball",cursive;font-size:110px;color:var(--plum);line-height:1.1}
  .tagline{position:absolute;top:140px;width:100%;text-align:center;font-family:"Playball",cursive;font-size:42px;color:var(--rose)}
  .invite{position:absolute;top:210px;width:100%;text-align:center;font-weight:700;font-size:24px}
  .swoosh{position:absolute;top:225px;left:0}
  .details{position:absolute;top:345px;left:0;width:960px;height:170px}
  .detail{position:absolute;top:0;height:170px;background:var(--box-bg);border:2px solid var(--blush);border-radius:16px;text-align:center;font-size:20px;line-height:1.6}
  .detail h3{font-family:"Playball",cursive;font-weight:400;color:var(--blue);font-size:30px;margin:18px 0 6px}
  .detail--when{left:50px;width:150px}
  .detail--time{left:236px;width:244px}
  .detail--where{left:516px;width:394px;font-size:19px}
  .speakers{position:absolute;top:555px;left:0;width:960px;height:170px;background:var(--band);text-align:center;color:var(--white);font-size:21px;line-height:1.75}
  .speakers h2{font-family:"Playball",cursive;font-weight:400;color:var(--yellow);font-size:32px;margin:6px 0 2px}
  .speakers .name{color:var(--yellow);font-weight:600;margin-right:12px}
  .tickets{position:absolute;top:745px;left:40px;width:420px;text-align:center}
  .tickets h2{font-size:50px;font-weight:700;color:var(--orchid);line-height:1}
  .price{font-size:66px;font-weight:700;color:var(--orchid);line-height:1.1}
  .price small{font-size:40px;font-weight:400}
  .drinks{font-size:30px;margin-top:2px}
  .guest{font-size:22px;margin-top:14px}
  .contact{position:absolute;top:755px;left:500px;width:440px;text-align:center}
  .contact h2{font-size:27px;font-weight:600;color:var(--orchid);line-height:1.25}
  .contact .line{font-size:23px;margin-top:4px}
  .contact .phone{font-weight:700}
  .contact svg{display:block;margin:22px auto 0}
  .sendoff{position:absolute;top:952px;left:339px;width:282px;height:52px;background:var(--orchid);color:var(--white);font-family:"Playball",cursive;font-size:30px;text-align:center;line-height:52px}
  .gallery{position:absolute;top:940px;left:0}
</style>
</head>
<body>
<main class="flyer">
  <h1 class="title">Get The 411</h1>
  <p class="tagline">Open Yourself Up To The Info You Have Inside</p>
  <p class="invite">Please Join Us For An Evening of Self Discovery, and Enlightment and Fun!</p>

  <svg class="swoosh" width="960" height="100" viewBox="0 0 960 100">
    <path d="M0 0 Q480 140 960 40" fill="none" stroke="#d2a4cc" stroke-width="4"/>
    <path d="M0 40 Q480 130 960 0" fill="none" stroke="var(--orchid)" stroke-width="4"/>
  </svg>

  <section class="details">
    <div class="detail detail--when"><h3>When:</h3>Thursday<br>11th April</div>
    <div class="detail detail--time"><h3>Time:</h3>Doors Open at 5:30.<br>Event from 6pm-8pm.</div>
    <div class="detail detail--where"><h3>Where:</h3>The Gardens at Palm Cove-<br>12345 Coastal Highway Islamorada<br>(MM80 Bayside behind Harbor Market)</div>
  </section>

  <section class="speakers">
    <h2>Speakers:</h2>
    <p><span class="name">Marisa Vale-</span>The Bright Path Life Coach- Certified Professional Life Coach</p>
    <p><span class="name">Celia Brandt-</span>Licensed Hypnotherapist- Moonstone Holistic Gifts and Therapies</p>
    <p><span class="name">Joan Sorrel-</span>Tarot Readings/ Clearwater Spiritual Counselor</p>
  </section>

  <section class="tickets">
    <h2>TICKETS</h2>
    <p class="price">$15 <small>each</small></p>
    <p class="drinks">Drinks included.</p>
    <p class="guest">Names must be on the guest list</p>
  </section>

  <section class="contact">
    <h2>Contact Marisa Vale<br>for tickets:</h2>
    <svg width="20" height="14" viewBox="0 0 20 14"><rect x="1" y="1" width="18" height="12" fill="none" stroke="var(--orchid)" stroke-width="1.5"/><path d="M1 1 L10 8 L19 1 M1 13 L8 6 M19 13 L12 6" fill="none" stroke="var(--orchid)" stroke-width="1.5"/></svg>
    <p class="line">marisa@brightpathlifecoach.com</p>
    <svg width="20" height="20" viewBox="0 0 20 20" style="margin-top:8px"><circle cx="10" cy="10" r="8.5" fill="none" stroke="var(--orchid)" stroke-width="1.5"/><path d="M7 5.5 L8.5 8 L7.5 9 Q9 12 11 12.5 L12 11.5 L14.5 13 L13.5 14.5 Q8 14 5.5 7 Z" fill="var(--orchid)"/></svg>
    <p class="line phone">305-555-0147</p>
  </section>

  <div class="sendoff">Hope to see you there!</div>

  <svg class="gallery" width="960" height="260" viewBox="0 0 960 260">
    <defs>
      <linearGradient id="coachTone" x1="0" y1="0" x2="1" y2="1"><stop offset="0" stop-color="#f3ece4"/><stop offset="1" stop-color="#c9a27c"/></linearGradient>
      <linearGradient id="tarotTone" x1="0" y1="0" x2="1" y2="1"><stop offset="0" stop-color="#5a4a6a"/><stop offset="1" stop-color="#e8c14a"/></linearGradient>
      <linearGradient id="healTone" x1="0" y1="0" x2="1" y2="1"><stop offset="0" stop-color="#f4f1ee"/><stop offset="1" stop-color="#d9b8a2"/></linearGradient>
    </defs>
    <circle cx="172" cy="235" r="180" fill="none" stroke="var(--orchid)" stroke-width="5"/>
    <circle cx="172" cy="235" r="168" fill="url(#coachTone)" stroke="#f59296" stroke-width="3" role="img" aria-label="Photo of a life coaching session at a desk"/>
    <circle cx="480" cy="320" r="160" fill="var(--white)" stroke="var(--orchid)" stroke-width="5"/>
    <circle cx="480" cy="320" r="148" fill="url(#tarotTone)" stroke="#f59296" stroke-width="3" role="img" aria-label="Photo of tarot cards and a crystal pendulum"/>
    <circle cx="788" cy="235" r="180" fill="var(--white)" stroke="var(--orchid)" stroke-width="5"/>
    <circle cx="788" cy="235" r="168" fill="url(#healTone)" stroke="#f59296" stroke-width="3" role="img" aria-label="Photo of a woman relaxing during crystal healing therapy"/>
  </svg>
</main>
</body>
</html>
```